VPN Tech Comparison site. Clean and professional looking.

WORDPRESS

We need a website for "TunnelDesk" - A comparison website, news and article site.

We need a website that covers three main from top to bottom.

- Logo
- Menu underneath

- 5 Best of with a table of comparable features

then two columns, left column bigger, right column smaller

Right column to contain latest blog posts with thumbnails all the way down the same length as the left column.

Left column :

Separate section with each "Best for" in a separate section within.

- Best For Device ...

- Best for Country...

- Best for Features

Separate section with each "Latest" in a separate section within.

- Latest News

- Latest Reviews

- Latest Guides

- Latest Articles

Quite like the layout of http://www.vorbane.com/ so something along those lines, although not exactly and less graphically intense.

Target Market(s)

20-60 age range. Mostly male with some female.

Beginner friendly looking.

Industry/Entity Type

Information Technology

Number of Pages Required

2 page

Font styles to use
Sans Serif

Colors
32a6d6
33b8a4

Requirements
Must have
• 1 main page as described in the description.
• 1 blog post page with latest articles in a right side column.
Nice to have
• Easily readable font of a semi-big size for blog posts.
• Not overly graphical.

```html
<!DOCTYPE html>
<html lang="en">
<head>
<meta charset="utf-8">
<title>TunnelDesk – VPN Comparison, News and Articles</title>
<link href="https://fonts.googleapis.com/css2?family=Open+Sans:ital,wght@0,400;0,600;0,700;1,400&family=Noto+Serif:wght@400&display=swap" rel="stylesheet">
<style>
:root{
  --teal:#33b8a4;
  --blue:#32a6d6;
  --ink:#222;
  --text:#555;
  --muted:#999;
  --page:#efefef;
  --panel:#fff;
  --tile:#f0f0f0;
  --footer:#1f1f1f;
}
*{box-sizing:border-box;margin:0;padding:0}
html,body{width:1200px;height:3939px;overflow:hidden}
body{position:relative;background:var(--page);font-family:"Open Sans",Arial,sans-serif;color:var(--text)}

/* header */
.site-header{position:absolute;left:0;top:0;width:1200px;height:100px;background:var(--panel)}
.brand{position:absolute;left:74px;top:22px;font-weight:700;font-size:44px;color:var(--teal);letter-spacing:-1px}
.social{position:absolute;left:900px;top:26px;display:flex;gap:8px}
.social span,.foot-social span{position:relative;border-radius:50%}
.social span{width:40px;height:40px;border:2px solid #ccc}
.social span::after,.foot-social span::after{content:"";position:absolute;left:50%;top:50%;border-radius:50%;transform:translate(-50%,-50%)}
.social span::after{width:14px;height:14px;background:#ccc}
.main-nav{position:absolute;left:0;top:100px;width:1200px;height:42px;background:var(--teal)}
.main-nav ul{list-style:none;position:absolute;left:100px;top:0;display:flex;height:42px;align-items:center}
.main-nav li{color:#fff;font-size:13px;font-weight:700;margin-right:52px}
.search{position:absolute;left:945px;top:8px;width:210px;height:27px;background:#fff;border-radius:14px;font-size:11px;color:var(--muted);padding:5px 14px}

/* hero */
.hero .tile{position:absolute;overflow:hidden}
.hero .tile .cap{position:absolute;left:30px;bottom:22px;right:24px;color:#fff;font-weight:600;font-size:17px;line-height:23px}
.g1{background:linear-gradient(160deg,#b9c2cc,#4a5664)}
.g2{background:linear-gradient(180deg,#9fc2e2,#5d6f86 60%,#3b3f48)}
.g3{background:linear-gradient(150deg,#6f7e8c,#2f3a46)}
.g4{background:linear-gradient(170deg,#d8d2c8,#6d6257)}
.g5{background:linear-gradient(160deg,#c4b8a6,#5b4a3d)}

/* panels */
.content{position:absolute;left:58px;top:670px;width:814px;height:3110px;background:var(--panel)}
.sidebar{position:absolute;left:872px;top:670px;width:270px;height:1120px;background:var(--panel)}
.side-head{position:absolute;left:0;top:0;width:270px;height:60px;background:var(--teal);color:#fff;text-align:center;font-size:19px;line-height:60px}
.side-head::after{content:"";position:absolute;left:125px;top:60px;border:10px solid transparent;border-top-color:var(--teal)}
.post{position:absolute;left:16px;width:245px;height:100px}
.post .thumb{position:absolute;left:0;top:0;width:84px;height:84px}
.post p{position:absolute;left:102px;top:-2px;width:140px;font-size:12.5px;line-height:19px;color:var(--ink)}
.post small{position:absolute;left:102px;top:62px;font-size:9.5px;color:var(--muted)}

/* welcome */
.welcome-title{position:absolute;left:74px;top:708px;font-size:19px;color:var(--ink);font-weight:600}
.welcome-title b{color:var(--teal);font-size:40px;font-weight:700;margin-left:6px;letter-spacing:-1px}
.welcome-text{position:absolute;left:74px;top:772px;width:782px;font-size:13px;line-height:25px;color:var(--text)}

/* section heads */
.sec-head{position:absolute;left:74px;width:782px;text-align:center;font-family:"Noto Serif",Georgia,serif;font-size:23px;font-weight:400;color:var(--ink)}
.sec-head em{font-style:normal;color:var(--blue)}
.sec-head::after{content:"";position:absolute;left:0;top:42px;width:782px;height:1px;background:#9fd4cc}
.sec-head::before{content:"";position:absolute;left:381px;top:43px;border:10px solid transparent;border-top-color:var(--teal)}

/* cards */
.card-img{position:absolute;width:242px}
.card-txt{position:absolute;width:238px;font-size:13.5px;line-height:22px;color:var(--ink)}
.meta{position:absolute;font-size:10px;color:var(--muted)}
.dev{background:linear-gradient(180deg,#ececec,#d6d6d6)}

/* country */
.country .pic{position:absolute;width:152px;height:152px}
.country .place{position:absolute;font-size:11px;color:var(--muted)}
.country h4{position:absolute;width:175px;font-size:15px;line-height:22px;font-weight:400;color:var(--ink)}
.country p{position:absolute;width:175px;font-size:12.5px;line-height:22px;color:var(--muted)}

/* features */
.feature{position:absolute;left:74px;width:782px}
.feature svg{position:absolute;left:0;top:3px}
.feature p{position:absolute;left:36px;width:730px;font-size:13px;line-height:25px;color:var(--ink)}

/* reviews */
.quote{position:absolute;top:2805px;width:378px;height:168px;background:var(--tile);padding:22px 26px;font-style:italic;font-size:12.5px;line-height:24px;color:var(--text)}
.quote::after{content:"";position:absolute;left:40px;top:168px;border:12px solid transparent;border-top-color:var(--tile)}
.reviewer{position:absolute;top:2984px;font-size:14px;color:var(--ink)}
.reviewer small{display:block;font-size:10px;color:var(--muted)}

/* guides */
.guide{position:absolute;width:360px}
.guide svg{position:absolute;left:0;top:4px}
.guide p{position:absolute;left:22px;width:300px;font-size:13.5px;line-height:24px;color:var(--ink)}

/* footer */
.site-footer{position:absolute;left:0;top:3795px;width:1200px;height:144px;background:var(--footer)}
.foot-nav{position:absolute;left:0;top:30px;width:1200px;text-align:center;font-size:12px;color:#bbb}
.foot-nav span{margin:0 12px}
.foot-social{position:absolute;left:510px;top:64px;display:flex;gap:8px}
.foot-social span{width:32px;height:32px;border:2px solid #888}
.foot-social span::after{width:10px;height:10px;background:#888}
.copy{position:absolute;left:0;top:108px;width:1200px;text-align:center;font-size:11px;color:var(--teal)}
</style>
</head>
<body>

<header class="site-header">
  <div class="brand">TunnelDesk</div>
  <div class="social" aria-label="Social links"><span></span><span></span><span></span><span></span><span></span></div>
</header>
<nav class="main-nav">
  <ul><li>HOME</li><li>ABOUT</li><li>BEST FOR</li><li>NEWS</li><li>ARTICLES</li><li>REVIEW</li><li>CONTACT</li><li>BLOG</li></ul>
  <div class="search">Search</div>
</nav>

<section class="hero">
  <div class="tile g1" style="left:0;top:144px;width:433px;height:258px" role="img" aria-label="Photo of business team standing in city"><div class="cap">Lorem ipsum dolore magna aliquam erat volutpat. Ut wisi enim ...</div></div>
  <div class="tile g4" style="left:0;top:406px;width:433px;height:258px" role="img" aria-label="Photo of colleagues reviewing a document"><div class="cap">Lorem ipsum dolore magna aliquam erat volutpat. Ut wisi enim ...</div></div>
  <div class="tile g2" style="left:436px;top:144px;width:328px;height:520px" role="img" aria-label="Photo of a group seen from below against the sky"><div class="cap">Lorem ipsum dolore magna erat volutpat. Ut wisi enim ...</div></div>
  <div class="tile g3" style="left:767px;top:144px;width:433px;height:258px" role="img" aria-label="Photo of people working at a laptop"><div class="cap">Lorem ipsum dolore magna aliquam erat volutpat. Ut wisi enim ...</div></div>
  <div class="tile g5" style="left:767px;top:406px;width:433px;height:258px" role="img" aria-label="Photo of a businessman in an office"><div class="cap">Lorem ipsum dolore magna aliquam erat volutpat. Ut wisi enim ...</div></div>
</section>

<main class="content"></main>

<aside class="sidebar">
  <div class="side-head">Latest BLOG POSTS</div>
  <div class="post" style="top:90px"><div class="thumb g1" role="img" aria-label="Blog thumbnail photo"></div><p>Lorem Ipsum is simply dummy text of the printing...</p><small>20 Dec 2015 | 562 Comments</small></div>
  <div class="post" style="top:205px"><div class="thumb g3" role="img" aria-label="Blog thumbnail photo"></div><p>Lorem Ipsum is simply dummy text of the printing...</p><small>20 Dec 2015 | 562 Comments</small></div>
  <div class="post" style="top:320px"><div class="thumb g4" role="img" aria-label="Blog thumbnail photo"></div><p>Lorem Ipsum is simply dummy text of the printing...</p><small>20 Dec 2015 | 562 Comments</small></div>
  <div class="post" style="top:435px"><div class="thumb g1" role="img" aria-label="Blog thumbnail photo"></div><p>Lorem Ipsum is simply dummy text of the printing...</p><small>20 Dec 2015 | 562 Comments</small></div>
  <div class="post" style="top:550px"><div class="thumb g5" role="img" aria-label="Blog thumbnail photo"></div><p>Lorem Ipsum is simply dummy text of the printing...</p><small>20 Dec 2015 | 562 Comments</small></div>
  <div class="post" style="top:665px"><div class="thumb g3" role="img" aria-label="Blog thumbnail photo"></div><p>Lorem Ipsum is simply dummy text of the printing...</p><small>20 Dec 2015 | 562 Comments</small></div>
  <div class="post" style="top:780px"><div class="thumb g4" role="img" aria-label="Blog thumbnail photo"></div><p>Lorem Ipsum is simply dummy text of the printing...</p><small>20 Dec 2015 | 562 Comments</small></div>
  <div class="post" style="top:895px"><div class="thumb g2" role="img" aria-label="Blog thumbnail photo"></div><p>Lorem Ipsum is simply dummy text of the printing...</p><small>20 Dec 2015 | 562 Comments</small></div>
  <div class="post" style="top:1010px"><div class="thumb g1" role="img" aria-label="Blog thumbnail photo"></div><p>Lorem Ipsum is simply dummy text of the printing...</p><small>20 Dec 2015 | 562 Comments</small></div>
</aside>

<h1 class="welcome-title">Welcome to <b>TunnelDesk</b></h1>
<p class="welcome-text">Lorem Ipsum is simply dummy text of the printing and typesetting industry. Lorem Ipsum has been the industry's standard dummy text ever since the 1500s, when an unknown printer took a galley of type and scrambled it to make a type specimen book. It has survived not only five centuries, but also the leap into electronic typesetting, remaining essentially unchanged. It was popularised in the 1960s with the release of Typoset sheets containing Lorem Ipsum passages, and more recently with desktop publishing software like Quillset Layout including versions of Lorem Ipsum.</p>

<!-- Best for device -->
<h2 class="sec-head" style="top:940px">Best For <em>DEVICE</em></h2>
<div class="card-img dev" style="left:74px;top:1024px;height:302px" role="img" aria-label="Product photo of smartphones running a VPN app"></div>
<div class="card-img dev" style="left:344px;top:1024px;height:302px" role="img" aria-label="Product photo of phones showing a VPN app"></div>
<div class="card-img dev" style="left:614px;top:1024px;height:302px" role="img" aria-label="Product photo of phones with a usage chart app"></div>
<p class="card-txt" style="left:74px;top:1334px">Lorem Ipsum is simply dummy text of the printing...</p>
<p class="card-txt" style="left:344px;top:1334px">Lorem Ipsum is simply dummy text of the printing...</p>
<p class="card-txt" style="left:614px;top:1334px">Lorem Ipsum is simply dummy text of the printing...</p>

<!-- Best for country -->
<h2 class="sec-head" style="top:1428px">Best For <em>COUNTRY</em></h2>
<div class="country">
  <div class="pic" style="left:74px;top:1510px;background:linear-gradient(180deg,#1f2b52,#6a5a8a)" role="img" aria-label="Photo of a city bridge at night"></div>
  <span class="place" style="left:252px;top:1510px">London</span>
  <h4 style="left:252px;top:1532px">Lorem Ipsum is simply dummy text of printing...</h4>
  <p style="left:252px;top:1582px">Lorem Ipsum has been the ever since the 1500s,</p>
  <div class="pic" style="left:478px;top:1510px;background:linear-gradient(180deg,#2a3560,#c48a4a)" role="img" aria-label="Photo of a city skyline at dusk"></div>
  <span class="place" style="left:656px;top:1510px">Australia</span>
  <h4 style="left:656px;top:1532px">Lorem Ipsum is simply dummy text of printing...</h4>
  <p style="left:656px;top:1582px">Lorem Ipsum has been the ever since the 1500s,</p>
  <div class="pic" style="left:74px;top:1686px;background:linear-gradient(180deg,#5b8fc4,#8a6a4a)" role="img" aria-label="Photo of a clock tower in a capital city"></div>
  <span class="place" style="left:252px;top:1686px">UK, London</span>
  <h4 style="left:252px;top:1708px">Lorem Ipsum is simply dummy text of printing...</h4>
  <p style="left:252px;top:1758px">Lorem Ipsum has been the ever since the 1500s,</p>
  <div class="pic" style="left:478px;top:1686px;background:linear-gradient(180deg,#9bc0dc,#5d7d8f)" role="img" aria-label="Photo of a harbour statue and skyline"></div>
  <span class="place" style="left:656px;top:1686px">USA</span>
  <h4 style="left:656px;top:1708px">Lorem Ipsum is simply dummy text of printing...</h4>
  <p style="left:656px;top:1758px">Lorem Ipsum has been the ever since the 1500s,</p>
</div>

<!-- Best for features -->
<h2 class="sec-head" style="top:1893px">Best For <em>FEATURES</em></h2>
<div class="feature" style="top:1972px"><svg width="20" height="20" viewBox="0 0 20 20"><circle cx="10" cy="10" r="8.5" fill="none" stroke="#33b8a4" stroke-width="1.5"/><path d="M8 6l4 4-4 4" fill="none" stroke="#33b8a4" stroke-width="1.5"/></svg><p>Lorem Ipsum is simply dummy text of the printing and typesetting industry. Lorem Ipsum has been the industry's standard dummy text ever since the 1500s.</p></div>
<div class="feature" style="top:2033px"><svg width="20" height="20" viewBox="0 0 20 20"><circle cx="10" cy="10" r="8.5" fill="none" stroke="#33b8a4" stroke-width="1.5"/><path d="M8 6l4 4-4 4" fill="none" stroke="#33b8a4" stroke-width="1.5"/></svg><p>Lorem Ipsum is simply dummy text of the printing and typesetting industry. Lorem Ipsum has been the industry's standard dummy text ever since the 1500s.</p></div>
<div class="feature" style="top:2094px"><svg width="20" height="20" viewBox="0 0 20 20"><circle cx="10" cy="10" r="8.5" fill="none" stroke="#33b8a4" stroke-width="1.5"/><path d="M8 6l4 4-4 4" fill="none" stroke="#33b8a4" stroke-width="1.5"/></svg><p>Lorem Ipsum is simply dummy text of the printing and typesetting industry. Lorem Ipsum has been the industry's standard dummy text ever since the 1500s.</p></div>
<div class="feature" style="top:2155px"><svg width="20" height="20" viewBox="0 0 20 20"><circle cx="10" cy="10" r="8.5" fill="none" stroke="#33b8a4" stroke-width="1.5"/><path d="M8 6l4 4-4 4" fill="none" stroke="#33b8a4" stroke-width="1.5"/></svg><p>Lorem Ipsum is simply dummy text of the printing and typesetting industry. Lorem Ipsum has been the industry's standard dummy text ever since the 1500s.</p></div>
<div class="feature" style="top:2216px"><svg width="20" height="20" viewBox="0 0 20 20"><circle cx="10" cy="10" r="8.5" fill="none" stroke="#33b8a4" stroke-width="1.5"/><path d="M8 6l4 4-4 4" fill="none" stroke="#33b8a4" stroke-width="1.5"/></svg><p>Lorem Ipsum is simply dummy text of the printing and typesetting industry. Lorem Ipsum has been the industry's standard dummy text ever since the 1500s.</p></div>

<!-- Latest news -->
<h2 class="sec-head" style="top:2313px">Latest <em>NEWS</em></h2>
<div class="card-img g3" style="left:74px;top:2398px;height:189px" role="img" aria-label="Photo of a team meeting seen from above"></div>
<div class="card-img g5" style="left:344px;top:2398px;height:189px" role="img" aria-label="Photo of colleagues looking at a tablet"></div>
<div class="card-img g2" style="left:614px;top:2398px;height:189px" role="img" aria-label="Photo of a team working at laptops"></div>
<span class="meta" style="left:74px;top:2606px">20 Dec 2015</span>
<span class="meta" style="left:344px;top:2606px">20 Dec 2015</span>
<span class="meta" style="left:614px;top:2606px">20 Dec 2015</span>
<p class="card-txt" style="left:74px;top:2624px">Lorem Ipsum is simply dummy text of the printing...</p>
<p class="card-txt" style="left:344px;top:2624px">Lorem Ipsum is simply dummy text of the printing...</p>
<p class="card-txt" style="left:614px;top:2624px">Lorem Ipsum is simply dummy text of the printing...</p>

<!-- Latest reviews -->
<h2 class="sec-head" style="top:2723px">Latest <em>REVIEWS</em></h2>
<blockquote class="quote" style="left:74px">"It has survived not only five centuries, but also the leap into electronic typesetting, remaining essentially unchanged. It was popularised in the 1960s with the release of Typoset sheets containing Lorem Ipsum including versions of Lorem Ipsum."</blockquote>
<blockquote class="quote" style="left:478px">"It has survived not only five centuries, but also the leap into electronic typesetting, remaining essentially unchanged. It was popularised in the 1960s with the release of Typoset sheets containing Lorem Ipsum including versions of Lorem Ipsum."</blockquote>
<div class="reviewer" style="left:158px">Owen Harrow<small>Lorem ipsum dolor</small></div>
<div class="reviewer" style="left:562px">Owen Harrow<small>Lorem ipsum dolor</small></div>

<!-- Latest guides -->
<h2 class="sec-head" style="top:3075px">Latest <em>GUIDES</em></h2>
<div class="guide" style="left:74px;top:3158px"><svg width="14" height="14" viewBox="0 0 14 14"><path d="M1 7l4 4 8-9" fill="none" stroke="#33b8a4" stroke-width="2"/></svg><p>Lorem Ipsum is simply dummy text of the industry's standard text ever since the 1500s.</p></div>
<div class="guide" style="left:478px;top:3158px"><svg width="14" height="14" viewBox="0 0 14 14"><path d="M1 7l4 4 8-9" fill="none" stroke="#33b8a4" stroke-width="2"/></svg><p>Lorem Ipsum is simply dummy text of the industry's standard text ever since the 1500s.</p></div>
<div class="guide" style="left:74px;top:3230px"><svg width="14" height="14" viewBox="0 0 14 14"><path d="M1 7l4 4 8-9" fill="none" stroke="#33b8a4" stroke-width="2"/></svg><p>Lorem Ipsum is simply dummy text of the industry's standard text ever since the 1500s.</p></div>
<div class="guide" style="left:478px;top:3230px"><svg width="14" height="14" viewBox="0 0 14 14"><path d="M1 7l4 4 8-9" fill="none" stroke="#33b8a4" stroke-width="2"/></svg><p>Lorem Ipsum is simply dummy text of the industry's standard text ever since the 1500s.</p></div>
<div class="guide" style="left:74px;top:3302px"><svg width="14" height="14" viewBox="0 0 14 14"><path d="M1 7l4 4 8-9" fill="none" stroke="#33b8a4" stroke-width="2"/></svg><p>Lorem Ipsum is simply dummy text of the industry's standard text ever since the 1500s.</p></div>
<div class="guide" style="left:478px;top:3302px"><svg width="14" height="14" viewBox="0 0 14 14"><path d="M1 7l4 4 8-9" fill="none" stroke="#33b8a4" stroke-width="2"/></svg><p>Lorem Ipsum is simply dummy text of the industry's standard text ever since the 1500s.</p></div>

<!-- Latest articles -->
<h2 class="sec-head" style="top:3395px">Latest <em>ARTICLES</em></h2>
<div class="card-img g4" style="left:74px;top:3480px;height:189px" role="img" aria-label="Photo of a team around a desk"></div>
<div class="card-img g1" style="left:344px;top:3480px;height:189px" role="img" aria-label="Photo of a woman at a desk with a laptop"></div>
<div class="card-img g3" style="left:614px;top:3480px;height:189px" role="img" aria-label="Photo of an office workspace"></div>
<span class="meta" style="left:74px;top:3690px">20 Dec 2015 | 250 Comments</span>
<span class="meta" style="left:344px;top:3690px">20 Dec 2015 | 250 Comments</span>
<span class="meta" style="left:614px;top:3690px">20 Dec 2015 | 250 Comments</span>
<p class="card-txt" style="left:74px;top:3708px">Lorem Ipsum is simply dummy text of the printing...</p>
<p class="card-txt" style="left:344px;top:3708px">Lorem Ipsum is simply dummy text of the printing...</p>
<p class="card-txt" style="left:614px;top:3708px">Lorem Ipsum is simply dummy text of the printing...</p>

<footer class="site-footer">
  <div class="foot-nav"><span>HOME</span>|<span>ABOUT</span>|<span>BEST FOR</span>|<span>NEWS</span>|<span>ARTICLES</span>|<span>REVIEW</span>|<span>CONTACT</span>|<span>BLOG</span></div>
  <div class="foot-social" aria-label="Social links"><span></span><span></span><span></span><span></span><span></span></div>
  <div class="copy">©2015 TunnelDesk ALL RIGHTS RESERVED</div>
</footer>

</body>
</html>
```